K spot menu

single page
we are located right across from Marlow Field Gulls ballpark
Menu has to be double sided 11”x17”

APPETIZERS
Guacamole and Chips $14 HH $9
House-made guacamole and tortilla chips. Served with pico de gallo, queso fresco and salsa.

Home Run Nachos $18 HH $13
House-made tortilla chips smothered with Jack and cheddar cheeses, your choice of meat (seasoned ground beef, chicken, pork carnitas, or veggies, beans, and jalapeños. Served with sour cream, guacamole, pico de gallo and salsa.

Quesadilla 15 HH$10
Flour tortilla filled with Jack and cheddar cheeses, your choice of meat (seasoned ground beef, chicken, pork carnitas, or veggies. folded in half and cooked golden brown. Served with sour cream and guacamole.

Beef Sliders $15
Premium Angus beef, Jack cheese, sauteed onions, rajas, tomato, spring mix, house mayo and chipotle aioli on a brioche bun.

Chicken Strips $15 HH $10
House-battered and breaded chicken breast strips. Served with your choice of dressing and fries. SUB ONION RINGS +$3

Bosco Wings $15 HH $10
7 Jumbo-size drums and flats tossed in your choice of sauce (BBQ, buffalo, mango habanero, or lemon pepper) or dry. Served with carrots, celery sticks, and your choice of dressing.

Onion Rings $9
Jumbo onion rings. Served with your choice of dressing.

Mozzarella Sticks $10
7 Breaded and fried mozzarella cheese sticks. Served with marinara sauce and ranch dressing.

SALADS
All salads are served with your choice of dressing (Ranch, Blue cheese, Honey mustard, or Balsamic vinaigrette).

Dinner Salad $9
Mixed greens, tomatoes, onions, cheese and carrots.

Taco Salad $17
Large flour tortilla crispy shell filled with your choice of meat (seasoned ground beef, pork carnitas, chicken or veggies, beans, lettuce, tomatoes, jalapeños and cheese. Topped with sour cream, pico de gallo and salsa.

Ahi Tuna Salad $19
Pan-seared Ahi tuna steak (6 oz.) on a bed of spring mix, tomatoes, beets, orange slices and sesame seeds.

Salmon Salad $20
Pan-seared salmon filet, on a bed of mixed greens, tomatoes, onions, avocado slices, carrots and cheese.
BURGERS ( 8oz)
Served with fries. (add an egg +$2)
El Gran Tio Burger $17
Verified Hollin Beef patty, cheddar cheese, and caramelized onions, mayo, lettuce, tomato, avocado and a fried jalapeño.

All-American Burger $16
Verified Hollin Beef patty, Cheddar cheese, mayo, lettuce, tomato, onion and pickles.
- Add bacon +$3
- Add an egg +$2

Whiskey Burger $17
Verified Hollin Beef patty, bacon, caramelized onions and Swiss cheese, mayo and house-made Wade Corbin whiskey sauce.

Mushroom Swiss Burger $17
Verified Hollin Beef patty, mayo, Swiss cheese, bacon, and mushrooms on ciabatta bread.

Veggie Burger $16 (VG)
Black bean patty on a pretzel bun with mayo, lettuce, tomato, onion, pickles, and avocado.

Salmon Burger $17
Pan-seared salmon filet (6 oz.) on a pretzel bun with mayo, lettuce, tomato, avocado and chipotle aioli.

Grilled Chicken Sandwich $16
Mayo, grilled chicken breast on ciabatta bread with lettuce, tomato, onions, pickles, and avocado.

SOUTH OF THE BORDER
3 Street Tacos 12 HH $7
seasoned ground beef, pork carnitas, chicken or veggies, pico de gallo and salsa. ADD GUAC +$3

2-lb. Burrito $15
Flour tortilla wrapped around your choice of meat seasoned ground beef, pork, chicken, or veggies. rice, beans, guacamole, sour cream, salsa and Jack and cheddar cheeses.

Chile Colorado Burrito $16
Special Trim Beef simmered in a house-made Chile Colorado sauce, rice and beans wrapped in a flour tortilla. Topped with sour cream.

EVENT MENU
Home Run Nachos $18
House-made tortilla chips smothered with Jack and cheddar cheeses, your choice of meat (seasoned ground beef, pork, chicken or veggies. beans and jalapeños. Served with sour cream, guacamole, pico de gallo and salsa.

3 Street Tacos $12
Your choice of meat seasoned ground beef, pork carnitas, chicken, or veggies, pico de gallo and salsa.

2-lb. Burrito $15
Flour tortilla wrapped around your choice of meat (seasoned ground beef, pork carnitas or grilled chicken) or veggies, rice, beans, guacamole, sour cream, salsa and Jack and cheddar cheeses.

Quesadilla $15
Flour tortilla filled with Jack and cheddar cheeses, your choice of meat (seasoned ground beef, pork carnitas, chicken or veggies, folded in half and cooked golden brown. Served with guacamole, pico de gallo and sour cream.

Taco Salad $17

Bosco Wings $15
7 Jumbo-size drums and flats tossed in your choice of sauce (BBQ, buffalo, mango habanero, or lemon pepper) or dry. Served with carrot and celery sticks.

Chicken Strips $15
House-battered and breaded chicken breast strips. Served with fries and your choice dressing.

All-American Burger $16
Verified Hollin Beef patty, Cheddar cheese, with mayo, lettuce, tomato, onion and pickles.
- Add bacon +$3
- Add avocado +$3

Whiskey Burger $17
Verified Hollin Beef patty, bacon, caramelized onions and Swiss cheese, with mayo and house-made Wade Corbin whiskey sauce.

Veggie Burger $16
Black bean patty, with mayo, lettuce, tomato, onion, pickles and avocado.

SIDES
basket of French fries $7
Rice $5
Beans $5
Sour cream $1
Avocado $4
Guacamole $7
Salsa 4oz. $2
Dressing $1

HOUSE SPECIALTIES
Carne Asada Entrée $23
Charbroiled skirt steak, cooked to order. Served with rice, beans, pico de gallo, salsa, sour cream, guacamole and tortillas.

Chile Colorado Entrée $18
Special Trim Beef simmered in a house-made Chile Colorado sauce. Served with rice, beans, sour cream and tortillas.

Pork Shank (Wednesdays only, until sold out) $24
Slow-baked pork shank (fork tender and fall-off-the-bone moist). Served with rice, beans, pico de gallo, salsa and tortillas. Ask your server about availability.

BEVERAGES
Soft Drinks $3.50
Zuma, Light Zuma, Vale Fizz,
Juice $5
Orange, cranberry, pineapple, grapefruit
Milk $4

HAPPY HOUR
Mon- Fri 2-5pm & 10-Close
Any draft beer $2 off
Selected appetizers $5 off
Well drinks $2 off
Wine $2 off

Daily specials 11:30 am - 5 pm

Margarita Monday $2 off /Burgers 20%off
Tacos Tuesday $5 off /Tequila Cruz Ortega 1877 $19.42
Wing Wednesday $5 Off / whiskey $2 Off
Thirsty Thursday Any draft beer $5/Nachos $5 off
Emberlock Friday $6 shot /Chile colorado burrito 20%off
Saturday and Sunday Brunch 10am-1pm. Mimosas and Bloody Marrys

Please make sure that you put this note on both pages * *CONSUMING RAW OR UNDERCOOKED MEATS, POULTRY, SEAFOOD, SHELLFISH, OR EGGS MAY INCREASE YOUR RISK OF FOODBORNE ILLNESS, ESPECIALLY IF YOU HAVE CERTAIN MEDICAL CONDITIONS.

Items that have eggs or meet HAS TO BE MARKED WITH AN ASTERISK*

AUTOMATIC 20% GRATUITY ON GROUPS OF 5 OR MORE. ALL ORDERS TO GO +$1

Target Market(s)

Young crowd

Industry/Entity Type

Sports bar

Colors
FFC000
F8CF3A
FAE287
FDF2CF
FEFAEE

Requirements
Must have
• Entire menu
Nice to have
• Menu has to be simple bat VERY attractive

```html
<!DOCTYPE html>
<html lang="en">
<head>
<meta charset="utf-8">
<title>K Spot Sports Bar &amp; Grill — Menu</title>
<link href="https://fonts.googleapis.com/css2?family=Alfa+Slab+One&family=Lilita+One&family=Oswald:wght@500&family=Poppins:wght@400;600;700&display=swap" rel="stylesheet">
<style>
:root{
  --backdrop:#c9c9c9;
  --ink:#0f0f0f;
  --paper-text:#e9e9e9;
  --muted:#cfcfcf;
  --white:#ffffff;
  --brush:#b39558;
  --brush-light:#d2b67a;
  --amber:#FFC000;
  --price:#f5ad1b;
  --red:#e0141e;
  --body:'Poppins',sans-serif;
}
*{box-sizing:border-box;margin:0;padding:0}
html,body{width:1200px;height:1200px;overflow:hidden;background:var(--backdrop)}
body{position:relative;font-family:var(--body);color:var(--paper-text)}
.page{position:absolute;top:200px;width:516px;height:797px;overflow:hidden;
  background:linear-gradient(180deg,#2a2219 0%,#161310 32%,var(--ink) 55%,#141414 100%)}
.page--front{left:68px}
.page--back{left:622px;background:linear-gradient(180deg,#1d1a17 0%,#121212 30%,var(--ink) 100%)}
.abs{position:absolute}
.photo{position:absolute}

/* brand + masthead */
.brand{left:31px;top:46px;display:flex;align-items:center;gap:6px;font-family:var(--body);font-weight:700;font-size:24px;color:var(--white);letter-spacing:1px}
.brand-dot{width:10px;height:10px;border-radius:50%;background:var(--white)}
.masthead{left:289px;top:30px;width:196px;text-align:center}
.masthead-rule{height:2px;background:var(--white);margin:2px 0}
.masthead-title{font-family:'Alfa Slab One',serif;font-size:58px;line-height:1.05;color:var(--white);letter-spacing:2px}
.address-band{margin-top:3px;background:var(--white);color:var(--ink);font-family:'Oswald',sans-serif;font-weight:500;font-size:10.5px;white-space:nowrap;padding:3px 0;clip-path:polygon(0 0,100% 0,96% 50%,100% 100%,0 100%,4% 50%)}
.phone{font-family:var(--body);font-weight:700;font-size:10px;color:var(--white);margin-top:3px;display:flex;align-items:center;justify-content:center;gap:3px}

/* section headers */
.section-head{position:absolute;height:25px;background:linear-gradient(90deg,var(--brush) 0%,var(--brush-light) 55%,var(--brush) 100%);
  clip-path:polygon(3% 12%,20% 0,55% 6%,92% 0,100% 30%,97% 78%,80% 100%,40% 93%,8% 100%,0 65%);
  font-family:'Lilita One',sans-serif;font-size:13px;color:#fdf2cf;display:flex;align-items:center;justify-content:center;letter-spacing:.5px}

/* menu lists */
.item-name{font-weight:700;font-size:5.4px;color:var(--white);text-transform:uppercase;line-height:1.3}
.item-desc{font-size:5.1px;line-height:1.28;color:var(--muted)}
.price{font-weight:700;font-size:5.8px;color:var(--white)}
.hh{font-weight:700;font-size:5.8px;color:var(--price)}
.star{color:var(--amber);font-size:7px;position:absolute;left:-10px;top:-1px}

.price-grid{display:grid;grid-template-columns:395px 32px 48px}
.price-grid > div{padding-bottom:7.6px}
.price-grid .col-price,.price-grid .col-hh{border-left:1px dotted #8a6f2f;text-align:center;padding-top:6px}

.simple-list .row{display:flex;justify-content:space-between;gap:6px;padding-bottom:7px}
.simple-list .row .text{flex:1}
.mini-list .row{display:flex;justify-content:space-between;align-items:baseline;padding-bottom:1.6px;line-height:1.3}
.mini-list .item-name{font-size:5.2px}
.mini-list .hh{line-height:1.3}

.note{font-size:5px;line-height:1.3;color:var(--muted);text-transform:uppercase}
.gratuity{font-weight:600;font-size:6.8px;line-height:1.25;color:var(--white)}
.togo-badge{border-radius:50%;background:var(--red);color:var(--white);display:flex;flex-direction:column;align-items:center;justify-content:center;font-weight:700;text-align:center;transform:rotate(-12deg);line-height:1}

/* happy hour */
.pill{position:absolute;background:var(--white);color:var(--ink);font-weight:700;font-size:5.2px;padding:3px 10px;clip-path:polygon(2% 10%,100% 0,97% 50%,100% 100%,0 92%,3% 50%)}
.pill em{font-style:normal;color:var(--red)}
.hh-table{display:grid;grid-template-columns:94px 50px 68px 20px;row-gap:3px}
.hh-table span{font-weight:700;font-size:5.4px;color:var(--white)}
.hh-table .off{color:var(--price)}
.specials .row{display:flex;justify-content:space-between;padding-bottom:2.6px;font-weight:700;font-size:5.4px;color:var(--white)}
.specials .row b{color:var(--red)}
.brunch{font-weight:700;font-size:5.6px;color:var(--amber)}
</style>
</head>
<body>

<!-- FRONT -->
<section class="page page--front">
  <div class="photo" role="img" aria-label="Dim bar interior with chrome beer taps" style="left:0;top:0;width:516px;height:320px;background:radial-gradient(ellipse at 40% 20%,rgba(120,92,60,.55),rgba(40,30,22,.35) 45%,transparent 75%)"></div>

  <div class="photo" role="img" aria-label="Chicken strips with fries, loaded nachos and a taco salad bowl on fresh lettuce" style="left:0;top:672px;width:516px;height:125px;background:linear-gradient(100deg,#c99a4a 0%,#e7c98c 22%,#8fae4b 45%,#d9b469 62%,#b98a3e 82%,#6f9a36 100%)"></div>

  <div class="abs brand"><span class="brand-dot"></span>K SPOT</div>

  <header class="abs masthead">
    <div class="masthead-rule"></div>
    <div class="masthead-title">MENU</div>
    <div class="masthead-rule"></div>
    <div class="address-band">48 LARKMOOR AVE HARBOR CITY CA 90210</div>
    <div class="phone">
      <svg width="8" height="8" viewBox="0 0 24 24"><path fill="#fff" d="M6.6 10.8a15 15 0 006.6 6.6l2.2-2.2c.3-.3.7-.4 1-.2 1.1.4 2.3.6 3.6.6.6 0 1 .4 1 1V20c0 .6-.4 1-1 1A17 17 0 013 4c0-.6.4-1 1-1h3.5c.6 0 1 .4 1 1 0 1.3.2 2.5.6 3.6.1.3 0 .7-.2 1z"/></svg>
      555.014.2290
    </div>
  </header>

  <h2 class="section-head" style="left:26px;top:126px;width:135px">APPETIZERS</h2>
  <div class="abs price-grid" style="left:29px;top:159px">
    <div><div class="item-name">Guacamole and Chips</div><div class="item-desc">House-made guacamole and tortilla chips. Served with pico de gallo, queso fresco and salsa.</div></div>
    <div class="col-price price">$14</div><div class="col-hh hh">HH $9</div>
    <div><div class="item-name">Home Run Nachos</div><div class="item-desc">House-made tortilla chips smothered with Jack and cheddar cheeses, your choice of meat (seasoned ground beef,<br>chicken, pork carnitas, or veggies) beans and jalapeños. Served with sour cream, guacamole, pico de gallo and salsa.</div></div>
    <div class="col-price price">$18</div><div class="col-hh hh">HH $13</div>
    <div><div class="item-name">Quesadilla</div><div class="item-desc">Flour tortilla filled with Jack and cheddar cheeses, your choice of meat (seasoned ground beef, chicken, pork carnitas,<br>or veggies). folded in half and cooked golden brown. Served with sour cream and guacamole.</div></div>
    <div class="col-price price">$15</div><div class="col-hh hh">HH $10</div>
    <div><div class="item-name">Beef Sliders</div><div class="item-desc">Premium Angus beef, Jack cheese, sauteed onions, rajas, tomato, spring mix, house mayo and chipotle aioli on<br>a brioche bun.</div></div>
    <div class="col-price price"></div><div class="col-hh price">$15</div>
    <div><div class="item-name">Chicken Strips</div><div class="item-desc">House-battered and breaded chicken breast strips. Served with your choice of dressing and fries.<br>SUB ONION RINGS +$3</div></div>
    <div class="col-price price">$15</div><div class="col-hh hh">HH $10</div>
    <div><div class="item-name">Bosco Wings</div><div class="item-desc">7 Jumbo-size drums and flats tossed in your choice of sauce (BBQ, buffalo, mango habanero, or lemon pepper) or<br>dry. Served with carrots, celery sticks, and your choice of dressing.</div></div>
    <div class="col-price price">$15</div><div class="col-hh hh">HH $10</div>
    <div><div class="item-name">Onion Rings</div><div class="item-desc">Jumbo onion rings. Served with your choice of dressing.</div></div>
    <div class="col-price price"></div><div class="col-hh price">$9</div>
    <div><div class="item-name">Mozzarella Sticks</div><div class="item-desc">7 Breaded and fried mozzarella cheese sticks. Served with marinara sauce and ranch dressing.</div></div>
    <div class="col-price price"></div><div class="col-hh price">$10</div>
  </div>

  <h2 class="section-head" style="left:26px;top:382px;width:135px">SALADS</h2>
  <div class="abs simple-list" style="left:29px;top:417px;width:210px">
    <div class="row"><div class="text"><div class="item-name" style="text-transform:none">All salads are served with your choice of dressing</div><div class="item-desc">(Ranch, Blue cheese, Honey mustard, or Balsamic vinaigrette).</div></div></div>
    <div class="row"><div class="text"><div class="item-name">Dinner Salad</div><div class="item-desc">Mixed greens, tomatoes, onions, cheese and<br>carrots.</div></div><div class="hh">$9</div></div>
    <div class="row" style="padding-bottom:14px"><div class="text"><div class="item-name">Taco Salad</div><div class="item-desc">Large flour tortilla crispy shell filled with your choice of meat (seasoned ground beef, pork carnitas, chicken or veggies) beans, lettuce, tomatoes, jalapeños and cheese. Topped with sour cream, pico de gallo and salsa.</div></div><div class="hh">$17</div></div>
    <div class="row"><div class="text"><div class="item-name">Ahi Tuna Salad</div><div class="item-desc">Pan-seared Ahi tuna steak (6 oz.) on a bed of spring mix, tomatoes, beets, orange slices and sesame seeds.</div></div><div class="hh">$20</div></div>
    <div class="row"><div class="text"><div class="item-name">Salmon Salad</div><div class="item-desc">Pan-seared salmon filet, on a bed of mixed greens, tomatoes, onions, avocado slices and cheese.</div></div><div class="hh">$20</div></div>
  </div>

  <h2 class="section-head" style="left:261px;top:382px;width:200px">SOUTH OF THE BORDER</h2>
  <div class="abs" style="left:267px;top:418px;display:grid;grid-template-columns:145px 20px 30px">
    <div style="padding-bottom:8px"><div class="item-name" style="text-transform:none">3 Street Tacos</div><div class="item-desc">seasoned ground beef, pork carnitas, chicken or veggies, pico de gallo and salsa.<br>ADD GUAC +$3</div></div>
    <div class="price" style="border-right:1px dotted #8a6f2f;padding-top:2px">$12</div><div class="hh" style="padding-left:7px;padding-top:2px">HH$7</div>
    <div><div class="item-name">2-lb. Burrito</div><div class="item-desc">Flour tortilla wrapped around your choice of meat (seasoned ground beef, pork, chicken, or veggies). rice, beans, guacamole, sour cream, salsa and Jack and cheddar cheeses.</div></div>
    <div style="border-right:1px dotted #8a6f2f"></div><div class="hh" style="padding-left:7px;padding-top:2px">$15</div>
  </div>

  <h2 class="section-head" style="left:263px;top:518px;width:84px">SIDES</h2>
  <div class="abs mini-list" style="left:269px;top:549px;width:97px">
    <div class="row"><span class="item-name">Basket of French Fries</span><span class="hh">$7</span></div>
    <div class="row"><span class="item-name">Rice</span><span class="hh">$5</span></div>
    <div class="row"><span class="item-name">Beans</span><span class="hh">$5</span></div>
    <div class="row"><span class="item-name">Sour Cream</span><span class="hh">$1</span></div>
    <div class="row"><span class="item-name">Avocado</span><span class="hh">$4</span></div>
    <div class="row"><span class="item-name">Guacamole</span><span class="hh">$7</span></div>
    <div class="row"><span class="item-name">Salsa 4oz.</span><span class="hh">$2</span></div>
    <div class="row"><span class="item-name">Dressing</span><span class="hh">$1</span></div>
  </div>

  <h2 class="section-head" style="left:379px;top:518px;width:106px">BEVERAGES</h2>
  <div class="abs simple-list" style="left:384px;top:549px;width:98px">
    <div class="row"><div class="text"><div class="item-name">Soft Drinks</div><div class="item-desc">Zuma, Light Zuma, Vale Fizz</div></div><div class="hh">$3.50</div></div>
    <div class="row"><div class="text"><div class="item-name">Juice</div><div class="item-desc">Orange, cranberry, pineapple, grapefruit</div></div><div class="hh">$5</div></div>
    <div class="row"><div class="text"><div class="item-name">Milk</div></div><div class="hh">$4</div></div>
  </div>

  <p class="abs note" style="left:31px;top:607px;width:200px">* *Consuming raw or undercooked meats, poultry, seafood, shellfish, or eggs may increase your risk of foodborne illness, especially if you have certain medical conditions.</p>
  <p class="abs gratuity" style="left:31px;top:636px;width:120px">AUTOMATIC 20% GRATUITY ON GROUPS OF 5 OR MORE.</p>
  <div class="abs togo-badge" style="left:146px;top:629px;width:38px;height:38px"><span style="font-size:3.6px">ALL ORDER<br>TO GO</span><span style="font-size:11px">$1</span></div>
</section>

<!-- BACK -->
<section class="page page--back">
  <div class="photo" role="img" aria-label="Red martini and orange margarita cocktails on a bar counter" style="left:288px;top:0;width:228px;height:278px;background:radial-gradient(ellipse at 35% 55%,rgba(226,44,70,.75),transparent 45%),radial-gradient(ellipse at 72% 40%,rgba(245,170,30,.8),transparent 45%),linear-gradient(180deg,#2d2620,#151210)"></div>

  <div class="photo" role="img" aria-label="Plate of glazed chicken wings with carrots, celery and ranch on lettuce" style="left:0;top:665px;width:300px;height:132px;background:linear-gradient(110deg,#5f8f2c 0%,#e9e4d8 25%,#b9681f 50%,#d08a35 70%,#6e9b33 100%)"></div>
  <div class="photo" role="img" aria-label="Burger with pretzel bun, fried egg, cheese, tomato and red onion on lettuce" style="left:272px;top:600px;width:244px;height:197px;background:radial-gradient(ellipse at 60% 45%,#8a3a18 0%,#b8661f 30%,#f0b02a 45%,transparent 62%),linear-gradient(90deg,transparent 0%,#4f8a2a 30%,#5e962f 100%)"></div>

  <h2 class="section-head" style="left:27px;top:35px;width:96px">BURGERS</h2>
  <p class="abs" style="left:28px;top:68px;font-size:7.6px;font-weight:600;color:var(--white)"><span style="color:var(--amber)">★</span> Served with fries. <span style="color:var(--amber);font-weight:400">(add an egg +$2)</span></p>
  <div class="abs simple-list" style="left:38px;top:80px;width:237px">
    <div class="row"><div class="text"><div class="item-name">El Gran Tio Burger</div><div class="item-desc">Verified Hollin Beef patty, cheddar cheese, and caramelized onions, mayo, lettuce, tomato, avocado and a fried jalapeño.</div></div><div class="hh">$17</div></div>
    <div class="row" style="position:relative"><span class="star">★</span><div class="text"><div class="item-name">All-American Burger</div><div class="item-desc">Verified Hollin Beef patty, Cheddar cheese, mayo, lettuce, tomato, onion and pickles.<br>- Add bacon +$3<br>- Add an egg +$2</div></div><div class="hh">$16</div></div>
    <div class="row" style="position:relative"><span class="star">★</span><div class="text"><div class="item-name">Whiskey Burger</div><div class="item-desc">Verified Hollin Beef patty, bacon, caramelized onions and Swiss cheese, mayo and house-made Wade Corbin whiskey sauce.</div></div><div class="hh">$17</div></div>
    <div class="row" style="position:relative"><span class="star">★</span><div class="text"><div class="item-name">Mushroom Swiss Burger</div><div class="item-desc">Verified Hollin Beef patty, mayo, Swiss cheese, bacon, and mushrooms on ciabatta bread.</div></div><div class="hh">$17</div></div>
    <div class="row" style="position:relative"><span class="star">★</span><div class="text"><div class="item-name">Veggie Burger(VG)</div><div class="item-desc">Black bean patty on a pretzel bun with mayo, lettuce, tomato, onion, pickles, and avocado.</div></div><div class="hh">$16</div></div>
    <div class="row" style="position:relative"><span class="star">★</span><div class="text"><div class="item-name">Salmon Burger</div><div class="item-desc">Pan-seared salmon filet (6 oz.) on a pretzel bun with mayo, lettuce, tomato, avocado and chipotle aioli.</div></div><div class="hh">$17</div></div>
    <div class="row"><div class="text"><div class="item-name">Grilled Chicken Sandwich</div><div class="item-desc">Mayo, grilled chicken breast on ciabatta bread with lettuce, tomato, onions, pickles, and avocado.</div></div><div class="hh">$16</div></div>
  </div>

  <h2 class="section-head" style="left:27px;top:288px;width:133px">EVENT MENU</h2>
  <div class="abs simple-list" style="left:38px;top:326px;width:204px">
    <div class="row" style="padding-bottom:5px"><div class="text"><div class="item-name">Home Run Nachos</div><div class="item-desc">House-made tortilla chips smothered with Jack and cheddar cheeses, your choice of meat (seasoned ground beef, pork, chicken or veggies. beans and jalapeños. Served with sour cream, guacamole, pico de gallo and salsa.</div></div><div class="hh">$18</div></div>
    <div class="row" style="padding-bottom:5px"><div class="text"><div class="item-name">3 Street Tacos</div><div class="item-desc">Your choice of meat seasoned ground beef, pork carnitas, chicken, or veggies, pico de gallo and salsa.</div></div><div class="hh">$12</div></div>
    <div class="row" style="padding-bottom:5px"><div class="text"><div class="item-name">2-lb. Burrito</div><div class="item-desc">Flour tortilla wrapped around your choice of meat (seasoned ground beef, pork carnitas or chicken) or veggies, rice, beans, guacamole, sour cream, salsa and Jack and cheddar cheeses.</div></div><div class="hh">$15</div></div>
    <div class="row" style="padding-bottom:5px"><div class="text"><div class="item-name">Quesadilla</div><div class="item-desc">Flour tortilla filled with Jack and cheddar cheeses, your choice of meat (seasoned ground beef, pork carnitas, chicken or veggies, folded in half and cooked golden brown. Served with guacamole, pico de gallo and sour cream.</div></div><div class="hh">$15</div></div>
    <div class="row" style="padding-bottom:5px"><div class="text"><div class="item-name">Taco Salad</div><div class="item-desc">Large flour tortilla crispy shell filled with your choice of meat (seasoned ground beef, pork carnitas, chicken or veggies, beans, lettuce, tomatoes, jalapeños and cheese. Topped with sour cream, pico de gallo and salsa.</div></div><div class="hh">$17</div></div>
    <div class="row" style="padding-bottom:5px"><div class="text"><div class="item-name">Bosco Wings</div><div class="item-desc">7 Jumbo-size drums and flats tossed in your choice of sauce (BBQ, buffalo, mango habanero, or lemon pepper) or dry. Served with carrot and celery sticks.</div></div><div class="hh">$15</div></div>
    <div class="row" style="padding-bottom:5px"><div class="text"><div class="item-name">Chicken Strips</div><div class="item-desc">House-battered and breaded chicken breast strips. Served with fries and your choice dressing.</div></div><div class="hh">$15</div></div>
    <div class="row" style="padding-bottom:5px;position:relative"><span class="star">★</span><div class="text"><div class="item-name">All-American Burger</div><div class="item-desc">Verified Hollin Beef patty, Cheddar cheese, with mayo, lettuce, tomato, onion and pickles.<br>- Add bacon +$3<br>- Add avocado +$3</div></div><div class="hh">$16</div></div>
    <div class="row" style="padding-bottom:5px"><div class="text"><div class="item-name">Whiskey Burger</div><div class="item-desc">Verified Hollin Beef patty, bacon, caramelized onions and Swiss cheese, with mayo and house-made Wade Corbin whiskey sauce.</div></div><div class="hh">$17</div></div>
    <div class="row"><div class="text"><div class="item-name">Veggie Burger</div><div class="item-desc">Black bean patty, with mayo, lettuce, tomato, onion, pickles and avocado.</div></div><div class="hh">$16</div></div>
  </div>

  <h2 class="section-head" style="left:253px;top:331px;width:118px">HAPPY HOUR</h2>
  <div class="pill" style="left:369px;top:338px;width:113px">Mon- Fri <em>2-5pm</em> &amp; <em>10-Close</em></div>
  <div class="abs hh-table" style="left:256px;top:366px">
    <span>ANY DRAFT BEER</span><span class="off">$2 OFF</span><span>WELL DRINKS</span><span class="off">$2 OFF</span>
    <span>SELECTED APPETIZERS</span><span class="off">$5 OFF</span><span>WINE</span><span class="off">$2 OFF</span>
  </div>

  <div class="pill" style="left:253px;top:401px;width:115px;font-size:4.8px">Daily specials <em>11:30 am - 5 pm</em></div>
  <div class="abs specials" style="left:256px;top:417px;width:232px">
    <div class="row"><span>MARGARITA MONDAY $2 OFF /BURGERS</span><b>$2 OFF</b></div>
    <div class="row"><span>TACOS TUESDAY $5 OFF /TEQUILA</span><b>$2 OFF</b></div>
    <div class="row"><span>WING WEDNESDAY $5 OFF / WHISKEY</span><b>$2 OFF</b></div>
    <div class="row"><span>THIRSTY THURSDAY BEER BUCKETS</span><b>$25</b></div>
    <div class="row"><span>EMBERLOCK FRIDAY $6 SHOT</span><b>$6 SHOTS</b></div>
    <p class="brunch">Saturday and Sunday Brunch 10am-1pm. Mimosas and Bloody Marrys</p>
  </div>

  <p class="abs note" style="left:256px;top:520px;width:150px;font-size:6.2px;color:var(--white)">* *Consuming raw or undercooked meats, poultry, seafood, shellfish, or eggs may increase your risk of foodborne illness, especially if you have certain medical conditions.</p>
  <div class="abs togo-badge" style="left:418px;top:498px;width:58px;height:58px"><span style="font-size:5.5px">ALL ORDER<br>TO GO</span><span style="font-size:16px">+$1</span></div>
  <p class="abs" style="left:256px;top:568px;font-size:7.6px;color:var(--amber)">All cards left over night Automatic 20% Gratuity</p>
</section>

</body>
</html>
```